KMT Compliant Dietary Supplement Label for Nutritional Company

We are in need of a label for our line of 20+ dietary supplements that are specifically formulated to balance body chemistry and match the biochemical individuality of our users based on hair tissue mineral analysis.

We have a line of approximately 20 different dietary supplements that will require use of new label in both a small (90 capsule) and large (180 capsule) size. We will start with the initial label in which Product name, Supplement Facts, and Ingredient list will need to be modified for each particular product thereafter.

The label will be placed on a transparent blue bottle with the color of lid being decided after label design. We are open to a transparent light amber bottle with black lid but blue is our preference.

We would like the majority of the label to be blue. Solid blue, fading of blue to darker blue/black, or subtle background designs are welcome with involvement of white and hints of orange. We do not want pictorial images on the label.

Label size:
Small bottle (120cc): Label size ~ 2.25” x 5.875”
Large bottle (200cc): Label size ~ 2.75” x 7.625”

Front:
-Logo near top of label with product name and description in middle and capsule count near the bottom

Right Side:
-Supplement Facts: See current product image below in brief
-Ingredient list: See current product image below in brief
-Manufactured for: See image below (This is on the left side of our current bottle and would like it moved to the bottom of the right side)

Left side:
-Suggested use: See current product image below in brief
-Leave room for possible warning statement
-Leave room for possible lot number printing
-Keep out of the reach of children.

The first files below are our current supplement label with product information. This information is what is needed on the label and will likely need some adjustments as we are updating our line of supplements and changes in KMT requirements.

The following files are the logo files and color palette.

The remaining files are some designs we came across for inspiration.

Thank you.

Target Market(s)

Health Care Profressionals

Industry/Entity Type

Health Care and Nutrition

Requirements
Nice to have
• Product name needs to be on same line in all one color
Should not have
• Pictorial Images

```html
<!DOCTYPE html>
<html lang="en">
<head>
<meta charset="utf-8">
<title>ADRAVEX Adrenal Supplement Label</title>
<link href="https://fonts.googleapis.com/css2?family=Montserrat:wght@400;500;600;700;800&family=Roboto:wght@400;500;700&display=swap" rel="stylesheet">
<style>
  :root {
    --blue: #2f5cab;
    --blue-deep: #23478f;
    --blue-light: #3d6cc0;
    --navy: #1f3f7a;
    --orange: #f08a24;
    --white: #ffffff;
    --silver: #c9ced6;
    --silver-light: #eef1f4;
    --stage: #e3e8ed;
  }
  * { box-sizing: border-box; margin: 0; padding: 0; }
  html, body { width: 1200px; height: 945px; overflow: hidden; }
  body {
    background: var(--stage);
    font-family: "Roboto", Arial, sans-serif;
    display: flex; align-items: center; justify-content: center;
  }
  .label {
    width: 1140px; height: 430px;
    display: flex; flex-direction: column;
    background: linear-gradient(180deg, var(--silver-light), var(--silver));
    box-shadow: 0 6px 20px rgba(0,0,0,.12);
  }
  .label-body { flex: 1; display: flex; margin: 14px 0; min-height: 0; }
  .panel { height: 100%; position: relative; }
  .panel-blue {
    background: linear-gradient(135deg, var(--blue-light) 0%, var(--blue) 45%, var(--blue-deep) 100%);
    color: var(--white);
  }
  /* left side */
  .panel-left { width: 393px; padding: 20px 36px 0 30px; }
  .distributor { text-align: right; }
  .distributor .lead { color: var(--orange); font-size: 20px; line-height: 1.2; }
  .distributor .name { color: var(--orange); font-size: 19px; font-weight: 700; line-height: 1.25; }
  .distributor .city { font-size: 18px; line-height: 1.3; }
  .divider { height: 1px; background: rgba(255,255,255,.7); margin: 12px 0 10px; }
  .suggested-use { text-align: right; font-size: 15.5px; line-height: 1.35; }
  .notice {
    position: absolute; left: 52px; right: 22px; bottom: 24px;
    background: var(--orange); padding: 10px 12px;
    font-size: 15.5px; line-height: 1.35;
  }
  /* front */
  .panel-front {
    width: 331px; background: var(--white);
    display: flex; flex-direction: column; align-items: center;
    font-family: "Montserrat", Arial, sans-serif;
  }
  .brand { margin-top: 40px; display: flex; flex-direction: column; align-items: center; }
  .brand-row { display: flex; align-items: center; gap: 8px; }
  .brand-dot { width: 16px; height: 16px; border-radius: 50%; background: var(--orange); }
  .brand-name { font-size: 34px; font-weight: 600; color: var(--blue); letter-spacing: 1px; }
  .brand-sub { font-size: 12px; letter-spacing: 4px; color: var(--blue); margin-top: 2px; }
  .product-name { margin-top: 46px; font-size: 46px; font-weight: 800; color: var(--blue); letter-spacing: .5px; }
  .product-desc { margin-top: 10px; font-size: 12px; font-weight: 700; letter-spacing: 1.6px; color: var(--navy); }
  .count { margin-top: auto; margin-bottom: 18px; display: flex; align-items: center; gap: 6px; }
  .count-num { background: var(--orange); color: var(--white); font-weight: 800; font-size: 15px; padding: 2px 7px; border-radius: 2px; }
  .count-unit { font-size: 14px; font-weight: 700; color: var(--navy); letter-spacing: 1px; }
  /* right side */
  .panel-right {
    width: 416px; padding: 12px 36px 14px 42px;
    display: flex; flex-direction: column; align-items: flex-start;
  }
  .facts-title {
    font-family: "Montserrat", Arial, sans-serif;
    color: var(--orange); font-size: 23px; font-weight: 700; line-height: 1.1;
  }
  .serving { font-size: 10.5px; font-weight: 700; line-height: 1.3; margin-top: 2px; }
  .facts { width: 100%; border-collapse: collapse; margin-top: 3px; font-size: 9.5px; }
  .facts th {
    text-align: left; font-weight: 700; padding: 2px 2px; line-height: 1.1;
    border-top: 4px solid var(--white); border-bottom: 1px solid var(--white);
  }
  .facts td { padding: 2px 2px; border-bottom: 1px solid rgba(255,255,255,.85); line-height: 1.12; vertical-align: middle; }
  .facts .col-amt { width: 72px; }
  .facts .col-dv { width: 58px; }
  .facts tr.rule-top td { border-top: 3px solid var(--white); }
  .facts .dv-note td { border-bottom: 3px solid var(--white); }
  .other { font-size: 9.5px; line-height: 1.3; margin-top: 4px; }
  .other span { color: var(--orange); }
  .manufacturer {
    margin-top: auto; white-space: nowrap;
    background: var(--orange); padding: 4px 8px; font-size: 9.5px; line-height: 1.3;
  }
</style>
</head>
<body>
  <main class="label">
    <div class="label-body">
      <section class="panel panel-blue panel-left">
        <div class="distributor">
          <p class="lead">Distributed by:</p>
          <p class="name">NOVAKIN LABORATORIES, INC.</p>
          <p class="city">Mesa, AZ 85201 USA</p>
        </div>
        <div class="divider"></div>
        <p class="suggested-use"><strong>SUGGESTED USE:</strong> One capsule<br>daily or as directed by a physician.</p>
        <p class="notice"><strong>NOTICE:</strong> It is advisable to keep this and all supplements out of the reach of children.</p>
      </section>

      <section class="panel panel-front">
        <div class="brand">
          <div class="brand-row">
            <span class="brand-dot"></span>
            <span class="brand-name">NOVAKIN</span>
          </div>
          <span class="brand-sub">LABORATORIES</span>
        </div>
        <h1 class="product-name">ADRAVEX</h1>
        <p class="product-desc">ADRENAL SUPPLEMENT</p>
        <div class="count"><span class="count-num">90</span><span class="count-unit">CAPSULES</span></div>
      </section>

      <section class="panel panel-blue panel-right">
        <h2 class="facts-title">Supplement Facts</h2>
        <p class="serving">Serving Size: 1 Capsule<br>Servings Per Container 90</p>
        <table class="facts">
          <thead>
            <tr><th></th><th class="col-amt">Amount<br>Per</th><th class="col-dv">%Daily<br>Serving</th></tr>
          </thead>
          <tbody>
            <tr><td>Vitamin C (as ascorbic acid)</td><td>100 mg</td><td>111%</td></tr>
            <tr><td>Vitamin B5<br>(as D-calcium pantothenate)</td><td>100 mg</td><td>2000%</td></tr>
            <tr><td>Magnesium (as magnesium<br>amino acid chelate)</td><td>5 mg</td><td>1%</td></tr>
            <tr><td>Zinc (as zinc amino acid chelate)</td><td>1 mg</td><td>9%</td></tr>
            <tr><td>Manganese (as manganese<br>amino acid chelate)</td><td>1 mg</td><td>43%</td></tr>
            <tr><td>Potassium (as potassium<br>amino acid chelate)</td><td>25 mg</td><td>1%</td></tr>
            <tr class="rule-top"><td>Suprarenal (adrenal) powder (bovine)</td><td>100 mg</td><td></td></tr>
            <tr><td>Liver powder, defatted (bovine)</td><td>45 mg</td><td></td></tr>
            <tr><td>Betaine Hydrochloride</td><td>25 mg</td><td></td></tr>
            <tr class="dv-note"><td colspan="3">Daily Value not established</td></tr>
          </tbody>
        </table>
        <p class="other"><span>Other Ingredients:</span> Hypromellose (Vegetable Capsule),<br>RiceFlo (Organic Rice Fiber)</p>
        <p class="manufacturer">Manufactured for: NOVAKIN LABORATORIES, INC.<br>Mesa, AZ 85201 USA</p>
      </section>
    </div>
  </main>
</body>
</html>
```